Business Card Design Project

Business card for law firm
Use existing logo
Must have:
Gerald P. Whitcombe
2715-C West 6th
Corvale, ST 78521
gwhitcombe@dvlegalgroup.com
www.dvlegalgroup.com
555-412-3095

Target Market(s)

Clients and potential clients, generally adult, business background

Industry/Entity Type

Business

Requirements
Must have
• Our logo, see below

```html
<!DOCTYPE html>
<html lang="en">
<head>
<meta charset="utf-8">
<title>Dunmore Vance — Business Card</title>
<link href="https://fonts.googleapis.com/css2?family=Cinzel:wght@400;700&display=swap" rel="stylesheet">
<style>
  :root {
    --page: #f1f1f1;
    --card-light: #ffffff;
    --card-dark: #231f20;
    --band: #5f5d5d;
    --ink: #3a3838;
    --mark: #6b6969;
    --on-dark: #ffffff;
    --divider: #7a7777;
  }
  * { margin: 0; padding: 0; box-sizing: border-box; }
  html, body {
    width: 1200px; height: 1000px; overflow: hidden;
    background: var(--page);
    font-family: "Cinzel", serif;
  }
  .card {
    position: absolute; left: 158px; top: 170px;
    width: 926px; height: 527px;
    background: var(--card-light);
  }
  .brand {
    position: absolute; left: 143px; top: 117px;
    height: 80px;
    display: flex; align-items: center;
  }
  .brand-square {
    width: 80px; height: 80px; background: var(--mark);
    margin-right: 16px;
  }
  .brand-name {
    font-size: 48px; font-weight: 400; color: var(--ink);
    line-height: 1; letter-spacing: 1px; white-space: nowrap;
  }
  .band {
    position: absolute; left: 0; top: 279px; width: 100%; height: 20px;
    background: var(--band);
  }
  .details {
    position: absolute; left: 0; top: 299px; width: 100%; height: 228px;
    background: var(--card-dark); color: var(--on-dark);
  }
  .person-name {
    position: absolute; left: 71px; top: 45px;
    font-size: 22px; font-weight: 700; letter-spacing: 0.5px;
    white-space: nowrap;
  }
  .contact {
    position: absolute; top: 124px;
    font-size: 18px; line-height: 26px; letter-spacing: 0.5px;
    white-space: nowrap;
  }
  .contact-address { left: 71px; }
  .contact-phone { left: 348px; }
  .contact-web { left: 531px; }
  .divider {
    position: absolute; top: 116px; width: 1px; height: 69px;
    background: var(--divider);
  }
  .divider-first { left: 318px; }
  .divider-second { left: 512px; }
</style>
</head>
<body>
  <div class="card">
    <div class="brand">
      <div class="brand-square"></div>
      <div class="brand-name">Dunmore Vance</div>
    </div>
    <div class="band"></div>
    <div class="details">
      <div class="person-name">GERALD P. WHITCOMBE</div>
      <div class="contact contact-address">2715-C West 6th<br>Corvale,&nbsp; ST&nbsp; 78521</div>
      <div class="divider divider-first"></div>
      <div class="contact contact-phone">555-412-3095</div>
      <div class="divider divider-second"></div>
      <div class="contact contact-web">gwhitcombe@dvlegalgroup.com<br>www.dvlegalgroup.com</div>
    </div>
  </div>
</body>
</html>
```